Business card design for engineering firm specializing in defense industry.

We need a professional business card design. Something simple but stands out. We are an engineering company specializing in composites in the defense industry.
Industry/Entity Type
Defense
Contact Information for Business Card
A simple black business card with the Varlonix yellow color is what we had in mind but open for other designs.
Colors
ffc214

```html
<!DOCTYPE html>
<html lang="en">
<head>
<meta charset="utf-8">
<title>Varlonix Business Card</title>
<link href="https://fonts.googleapis.com/css2?family=Poppins:wght@400;600;700;800&display=swap" rel="stylesheet">
<style>
  :root {
    --brand-yellow: #ffc214;
    --ink: #111111;
    --paper: #ffffff;
    --backdrop: #2b2d31;
  }
  * { box-sizing: border-box; margin: 0; padding: 0; }
  html, body {
    width: 1200px; height: 900px; overflow: hidden;
    background: var(--backdrop);
    font-family: "Poppins", sans-serif;
  }
  .stage {
    width: 1200px; height: 900px;
    display: flex; flex-direction: column; align-items: center; justify-content: center;
    gap: 40px;
  }
  .card {
    width: 560px; height: 320px;
    border-radius: 22px;
    overflow: hidden;
    position: relative;
  }
  /* Front */
  .card-front {
    background: var(--paper);
    display: flex; align-items: center; justify-content: center; gap: 22px;
  }
  .brand-square {
    width: 46px; height: 46px; background: var(--brand-yellow);
  }
  .brand-name {
    font-weight: 800; font-size: 68px; color: var(--ink); letter-spacing: 1px;
  }
  /* Back */
  .card-back { background: var(--paper); }
  .back-field {
    position: absolute; left: 0; top: 0; width: 100%; height: 238px;
    background: var(--brand-yellow);
  }
  .contact-block {
    position: absolute; left: 38px; top: 30px;
    color: var(--ink);
  }
  .person-name { font-weight: 800; font-size: 21px; letter-spacing: 0.5px; text-transform: uppercase; line-height: 1.1; }
  .person-role { font-size: 15px; font-weight: 400; margin-bottom: 16px; }
  .contact-list { list-style: none; }
  .contact-item {
    display: flex; align-items: center; gap: 10px;
    font-size: 15px; margin-bottom: 9px;
  }
  .contact-icon {
    width: 24px; height: 24px; border-radius: 50%; background: var(--ink);
    display: flex; align-items: center; justify-content: center; flex: none;
  }
  .back-mark {
    position: absolute; right: 40px; top: 70px;
    display: flex; align-items: center; gap: 14px;
  }
  .back-mark .brand-square { background: var(--ink); width: 40px; height: 40px; }
  .back-mark .brand-name { font-size: 48px; }
  .url-band {
    position: absolute; left: 0; top: 238px; width: 100%; height: 50px;
    display: flex; align-items: center; justify-content: center;
    font-weight: 700; font-size: 22px; letter-spacing: 6px; color: var(--ink);
  }
  .base-strip {
    position: absolute; left: 0; bottom: 0; width: 100%; height: 32px;
    background: var(--ink);
  }
  .base-strip::before {
    content: ""; position: absolute; left: 50%; top: -8px; margin-left: -8px;
    border-left: 8px solid transparent; border-right: 8px solid transparent;
    border-bottom: 8px solid var(--ink);
  }
</style>
</head>
<body>
<main class="stage">
  <section class="card card-front" aria-label="Card front">
    <span class="brand-square"></span>
    <span class="brand-name">Varlonix</span>
  </section>

  <section class="card card-back" aria-label="Card back">
    <div class="back-field"></div>
    <div class="contact-block">
      <p class="person-name">Marcus Hale</p>
      <p class="person-role">Director</p>
      <ul class="contact-list">
        <li class="contact-item">
          <span class="contact-icon">
            <svg width="13" height="13" viewBox="0 0 24 24"><path fill="#ffc214" d="M6.6 10.8a15.1 15.1 0 0 0 6.6 6.6l2.2-2.2c.3-.3.7-.4 1-.2 1.1.4 2.3.6 3.6.6.6 0 1 .4 1 1V20c0 .6-.4 1-1 1A17 17 0 0 1 3 4c0-.6.4-1 1-1h3.5c.6 0 1 .4 1 1 0 1.3.2 2.5.6 3.6.1.3 0 .7-.2 1z"/></svg>
          </span>
          +420 555 014 271
        </li>
        <li class="contact-item">
          <span class="contact-icon">
            <svg width="12" height="13" viewBox="0 0 24 24"><rect x="6" y="2" width="12" height="20" rx="2" fill="#ffc214"/><rect x="8" y="5" width="8" height="11" fill="#111"/></svg>
          </span>
          +420 555 014 388
        </li>
        <li class="contact-item">
          <span class="contact-icon">
            <svg width="13" height="11" viewBox="0 0 24 18"><rect x="1" y="1" width="22" height="16" rx="2" fill="#ffc214"/><path d="M2 2l10 8 10-8" fill="none" stroke="#111" stroke-width="2"/></svg>
          </span>
          Enquire@Varlonix.com
        </li>
      </ul>
    </div>
    <div class="back-mark">
      <span class="brand-square"></span>
      <span class="brand-name">Varlonix</span>
    </div>
    <div class="url-band">WWW.VARLONIX.COM</div>
    <div class="base-strip"></div>
  </section>
</main>
</body>
</html>
```